Quillfern Rise A4 Potrait foldout brochure

We need a brochure design for this residential land development. I have attached the a style that we like to base our design on. Full colour required. will provide files required for design also. PLEASE DO NOT COPY THIS DESIGN. Come up with a new style that gives you this feeling. Please note the plan needs to be positioned landscape on the inside 2 A4 Pages.

Industry/Entity Type

Residential

Font styles to use
Other font styles liked:
• Try with Century Gothich

Requirements
Must have
• use same colours as supplied in Quillfern rise brochure.
Nice to have
• nice modern simple background graphics

```html
<!DOCTYPE html>
<html lang="en">
<head>
<meta charset="utf-8">
<title>Quillfern Rise — Masterplan Brochure Cover</title>
<link rel="stylesheet" href="https://fonts.googleapis.com/css2?family=Didact+Gothic&display=swap">
<style>
  :root {
    --backdrop: #e3e3e3;
    --orange-light: #fbb21b;
    --orange-deep: #f7941d;
    --orange-strip: #f47f20;
    --green-light: #8dc63f;
    --green-mid: #5cb947;
    --green-dark: #0c4d2a;
    --green-forest: #004a22;
    --purple: #86479b;
    --yellow-light: #ffc20e;
    --yellow-deep: #f9a51b;
    --white: #ffffff;
    --accent-green: #7ac143;
  }
  html, body {
    margin: 0;
    padding: 0;
    width: 1200px;
    height: 849px;
    overflow: hidden;
    background: var(--backdrop);
    font-family: "Didact Gothic", "Century Gothic", sans-serif;
  }
  .cover {
    position: absolute;
    left: 345px;
    top: 57px;
    width: 524px;
    height: 724px;
    overflow: hidden;
    background: var(--green-forest);
  }
  .cover-terraces {
    position: absolute;
    inset: 0;
    width: 100%;
    height: 100%;
    display: block;
  }
  .cover-title {
    position: absolute;
    left: 40px;
    top: 392px;
    margin: 0;
    font-weight: 400;
    font-size: 52px;
    letter-spacing: 0.5px;
    color: var(--white);
    line-height: 1;
  }
  .brand {
    position: absolute;
    right: 42px;
    top: 652px;
    text-align: right;
  }
  .brand-name {
    display: block;
    font-size: 22px;
    color: var(--white);
    line-height: 1;
  }
  .brand-locale {
    display: block;
    margin-top: 4px;
    font-size: 7px;
    color: var(--accent-green);
    line-height: 1;
  }
</style>
</head>
<body>
  <main class="cover">
    <svg class="cover-terraces" viewBox="0 0 524 724" preserveAspectRatio="none" aria-hidden="true">
      <defs>
        <linearGradient id="orange-fade" x1="0" y1="0" x2="1" y2="1">
          <stop offset="0" stop-color="var(--orange-light)"/>
          <stop offset="1" stop-color="var(--orange-deep)"/>
        </linearGradient>
        <linearGradient id="yellow-fade" x1="0" y1="0" x2="1" y2="0">
          <stop offset="0" stop-color="var(--yellow-light)"/>
          <stop offset="1" stop-color="var(--yellow-deep)"/>
        </linearGradient>
        <linearGradient id="green-fade" x1="0" y1="0" x2="0" y2="1">
          <stop offset="0" stop-color="var(--green-light)"/>
          <stop offset="1" stop-color="var(--green-mid)"/>
        </linearGradient>
      </defs>
      <polygon class="terrace-sky" points="0,0 524,0 524,40 0,150" fill="url(#orange-fade)"/>
      <polygon class="terrace-accent" points="360,0 524,0 524,40 430,60" fill="var(--orange-strip)"/>
      <polygon class="terrace-purple" points="0,150 524,40 524,100 0,190" fill="var(--purple)"/>
      <polygon class="terrace-yellow" points="0,190 524,100 524,190 0,330" fill="url(#yellow-fade)"/>
      <polygon class="terrace-green" points="0,330 524,190 524,420 0,560" fill="url(#green-fade)"/>
      <polygon class="terrace-edge" points="0,560 524,420 524,432 0,574" fill="var(--green-mid)"/>
      <polygon class="terrace-shade" points="0,574 524,432 524,500 0,640" fill="var(--green-dark)"/>
    </svg>

    <h1 class="cover-title">Masterplan</h1>

    <div class="brand">
      <span class="brand-name">Quillfern Rise</span>
      <span class="brand-locale">Ashvale Park</span>
    </div>
  </main>
</body>
</html>
```